harbor lantern security & electric needs a business card

Must be attractive and modern, look professional and upscale!!
We provide alarm and cameras services and 24 hour monitoring for commercial and residential clients. In addition, the owner is a master electrician that provides services to commercial and residential clients.
We also install and service automatic gates. We previously had two different businesses but decided to merge into one, thus creating Harbor Lantern Security & Electric.

Target Market(s)

Commercial Business and residential customers

Industry/Entity Type

Security

Contact Information for Business Card

Front and back design with logo and services listed

Font styles to use
Sans Serif

Colors
ec1f27
0355a3
fbee3f

Requirements
Must have
• Front of card:
• Marcus Tremblow-Owner
• telephone icon and then the number 936-555-0193
• Mail icon and then email address mtremblow@quillmail.example
• World Icon then website www.yourharborlanterntx.example
• Location marker and then Cedar Hollow, Texas
• We would like to have a picture of the logo at least on the front
• Also need motto on front: We're There When You're Not
• The front of the card must also say Licensed and Insured in addition to:
• License Number: K47315
• TECL: 58629
• On the Back of the Card:
• List each of these Services with check marks:
• Residential and Commercial Electrical Services
• Electric Gates
• Alarm Systems
• Alarm Monitoring
• Cameras
• ***Use separate attached logo, the business card design is just to be used as a model***
Nice to have
• It would be nice to have the logo on back of the card in addition to these words at the bottom:
• "No job too big or small, we do it all!"
Should not have
• Anything crazy!!

```html
<!DOCTYPE html>
<html lang="en">
<head>
<meta charset="utf-8">
<title>Harbor Lantern Security &amp; Electric — Business Card</title>
<link href="https://fonts.googleapis.com/css2?family=Source+Sans+3:wght@400;600;700&display=swap" rel="stylesheet">
<style>
  :root{
    --canvas:#ebebeb;
    --card-white:#ffffff;
    --brand-blue:#4a66b3;
    --band-start:#4e6db5;
    --band-end:#7d95ca;
    --brand-red:#d93a44;
    --back-start:#666666;
    --back-end:#8a8a8a;
    --back-red:#de5a61;
    --back-blue:#7185b8;
  }
  *{margin:0;padding:0;box-sizing:border-box}
  html,body{width:1200px;height:824px;overflow:hidden;background:var(--canvas)}
  body{position:relative;font-family:"Source Sans 3",sans-serif}
  .card{position:absolute;top:261px;width:540px;height:302px;overflow:hidden;box-shadow:0 10px 28px rgba(0,0,0,.18)}
  .card-front{left:40px;background:var(--card-white)}
  .card-back{left:620px;background:linear-gradient(135deg,var(--back-start),var(--back-end))}

  .accent-bar{position:absolute;left:0;top:88px;width:64px;height:114px;background:var(--brand-red)}
  .contact-band{position:absolute;left:234px;right:0;top:88px;height:114px;background:linear-gradient(120deg,var(--band-start),var(--band-end))}

  .owner{position:absolute;left:288px;top:44px;color:var(--brand-blue);font-weight:700;font-size:22px;line-height:1.2;white-space:nowrap}
  .owner-title{color:var(--brand-red);font-weight:400;font-size:11px;margin-left:2px}

  .contact-list{position:absolute;left:262px;top:96px;list-style:none;color:#fff;font-size:11px}
  .contact-list li{display:flex;align-items:center;height:21px;gap:8px}
  .contact-list svg{width:11px;height:11px;flex:none}

  .brand{position:absolute;display:flex;align-items:center;gap:8px}
  .brand-mark{width:14px;height:14px;flex:none}
  .brand-name{font-weight:700;font-size:13px;line-height:1.15}
  .card-front .brand{left:88px;top:146px}
  .card-front .brand-mark{background:var(--brand-red)}
  .card-front .brand-name{color:var(--brand-blue)}

  .slogan{position:absolute;left:252px;top:212px;color:var(--brand-red);font-weight:700;font-size:12.5px;white-space:nowrap}

  .credentials{position:absolute;top:272px;color:var(--brand-blue);font-size:9.5px;white-space:nowrap}
  .credentials strong{font-weight:700}
  .cred-insured{left:80px}
  .cred-license{left:238px}
  .cred-tecl{left:424px}

  .services{position:absolute;left:290px;top:96px;list-style:none;color:var(--back-red);font-size:12px;line-height:16px}
  .services li{display:flex;gap:7px;margin-bottom:4px}
  .services svg{width:11px;height:11px;margin-top:3px;flex:none}

  .card-back .brand{left:90px;top:126px}
  .card-back .brand-mark{background:var(--back-red);opacity:.85}
  .card-back .brand-name{color:var(--back-blue)}

  .motto{position:absolute;left:50px;top:212px;color:var(--back-red);font-weight:700;font-size:12.5px;white-space:nowrap}
</style>
</head>
<body>
  <section class="card card-front" aria-label="Business card front">
    <div class="accent-bar"></div>
    <div class="contact-band"></div>

    <h1 class="owner">Marcus Tremblow <span class="owner-title">/ Owner</span></h1>

    <ul class="contact-list">
      <li>
        <svg viewBox="0 0 24 24" fill="#fff"><path d="M6.6 10.8a15 15 0 0 0 6.6 6.6l2.2-2.2c.3-.3.7-.4 1-.2 1.1.4 2.3.6 3.6.6.6 0 1 .4 1 1V20c0 .6-.4 1-1 1A17 17 0 0 1 3 4c0-.6.4-1 1-1h3.5c.6 0 1 .4 1 1 0 1.3.2 2.5.6 3.6.1.3 0 .7-.2 1z"/></svg>
        936-555-0193
      </li>
      <li>
        <svg viewBox="0 0 24 24" fill="#fff"><path d="M2 5h20v14H2z"/><path d="M2 5l10 8 10-8" fill="none" stroke="#5a78ba" stroke-width="2"/></svg>
        mtremblow@quillmail.example
      </li>
      <li>
        <svg viewBox="0 0 24 24" fill="none" stroke="#fff" stroke-width="2"><circle cx="12" cy="12" r="10"/><path d="M2 12h20M12 2c3 3 3 17 0 20M12 2c-3 3-3 17 0 20"/></svg>
        www.yourharborlanterntx.example
      </li>
      <li>
        <svg viewBox="0 0 24 24" fill="#fff"><path d="M12 2a7 7 0 0 0-7 7c0 5 7 13 7 13s7-8 7-13a7 7 0 0 0-7-7zm0 9.5A2.5 2.5 0 1 1 12 6.5a2.5 2.5 0 0 1 0 5z"/></svg>
        Cedar Hollow, Texas
      </li>
    </ul>

    <div class="brand">
      <span class="brand-mark"></span>
      <span class="brand-name">Harbor Lantern<br>Security &amp; Electric</span>
    </div>

    <p class="slogan">"No job too big or small, we do it all!"</p>

    <p class="credentials cred-insured">Licensed and Insured</p>
    <p class="credentials cred-license">License Number: <strong>K47315</strong></p>
    <p class="credentials cred-tecl">TECL: <strong>58629</strong></p>
  </section>

  <section class="card card-back" aria-label="Business card back">
    <ul class="services">
      <li><svg viewBox="0 0 24 24" fill="none" stroke="currentColor" stroke-width="4"><path d="M3 12l6 6L21 6"/></svg><span>Residential and Commercial<br>Electrical Services</span></li>
      <li><svg viewBox="0 0 24 24" fill="none" stroke="currentColor" stroke-width="4"><path d="M3 12l6 6L21 6"/></svg><span>Electric Gates</span></li>
      <li><svg viewBox="0 0 24 24" fill="none" stroke="currentColor" stroke-width="4"><path d="M3 12l6 6L21 6"/></svg><span>Alarm Systems</span></li>
      <li><svg viewBox="0 0 24 24" fill="none" stroke="currentColor" stroke-width="4"><path d="M3 12l6 6L21 6"/></svg><span>Alarm Monitoring</span></li>
      <li><svg viewBox="0 0 24 24" fill="none" stroke="currentColor" stroke-width="4"><path d="M3 12l6 6L21 6"/></svg><span>Cameras</span></li>
    </ul>

    <div class="brand">
      <span class="brand-mark"></span>
      <span class="brand-name">Harbor Lantern<br>Security &amp; Electric</span>
    </div>

    <p class="motto">We're There When You're Not</p>
  </section>
</body>
</html>
```